WORDPRESS WEB DESIGN PROJECT-DESIGN & DEVELOP

OUR BUSINESS
Bright Harbor Advisory provides effective project controls and management solutions for construction projects in Australia and Overseas. We provide services to both large multinational companies and smaller privately owned businesses. Our knowledge and expertise assist clients to effectively plan and manage their construction projects or project portfolios. Our focus is to provide your business with the tools, solutions and strategies necessary to deliver projects on time and within budget.

WHY WE ARE RE-BRANDING OUR WEBSITE
Our existing website design is not effective at promoting our business. We require a fresh, new, innovative approach to effectively market our business brand. Our new website will have the same look and feed as our newly developed business brochure.

DESIGN
Our new website will have the same look and feed as our business brochure. This website will be developed in Word press; a customized theme is required. The graphic design and images will enhance the written content; any graphics need to be developed in Photoshop as this is the software we use. A horizontal navigation menu will be implemented but must blend into the design and not be contained in a colour band. The webpage itself needs to span the entire viewable screen and must not look like an A4 piece of paper on a colored background. Additional design comments have been attached to this project as " website contents" word doc.

WEDSITES I LIKE THE LOOK OF
www.vantorelm.com (very professional, similar color scheme)
www.qurbikgear.com ( Good design, background made the website pop)
www.pelmorefloorwashing.com.au (clean,tidy,sharp images)
www.travelingua.com ( the look was simple but effective)
http://www.fendo-q.com

STYLE
We require a stylish, clean and easy to navigate website, with fresh, exciting and engaging imagery. Our website design needs to be modern, clean and sleek.

WRITTEN CONTENT
New written content for each page is provided with this project, there is 50% less content in this project than the original website.

QUALITY
High resolution images and photos will be used to promote an overall quality, professional look and feel.

FUNCTIONALITY
The design needs to be easily updated and editable. The person updating the webpage content and images does not know coding, so the theme will need to be able to interact with plugins. All design components need to be optimized for indexing on major search engines e.g. Firefox, internet explorer, Google and safari.

ICONS
I will require icon links to Email, Facebook and LinkedIn, but not for twitter, Gmail or live feeds.

MENU
1.Home
2.Services
3.Benefits
4.Management
5.Planning
6.Optimization
7.Industry
8.Software
9.Contact us
10.Recruitment

TARGET AUDIENCE
Corporate Clients in all industry’s sectors
Supporting clients in
★OIL & Gas
★Iron Ore
★Coal
★New Industries
★Building and Construction
★Rail
★Civil
★Manufacturing
★Petrochemical
★Telecommunications

THE WINNER WILL PROVIDE
1. Wordpress theme with design.
2. List of plugins needed to meet requirements or design.
3. All images used in design.
4. Any custom php, javascript, or css files needed for the design.
5. List of core wordpress files customized as part of the design.
6. Any source files for custom images or design work (psd)

ATTACHMENTS
The following items will be attached to this project
1. Business logo
2. Icon images
3. Business Brochure PDF
4. Business brochure cover page psd file
5. Content required in each webpage

DESIGN AND DEVELOP
This project is to design and develop a word press website. In respect that the chosen designer may not be able to provide the development, 2 places of $400 each have been offered (1st for the design aspect, and 2nd for the development). The winning designer will receive $800 if both design and development have been achieved.

PROJECT CHANGES

The projects budget has increased from $600 to $800

Completion date has extended by 7 day.

• This design must have not appear out-dated or cluttered
Please do not provide any designs that look like our old website.

```html
<!DOCTYPE html>
<html lang="en">
<head>
<meta charset="utf-8">
<title>Bright Harbor Advisory</title>
<link href="https://fonts.googleapis.com/css2?family=Open+Sans:wght@400;600;700&family=Noto+Serif:ital@1&display=swap" rel="stylesheet">
<style>
:root{
  --red:#e8221b;
  --orange:#ef4a1f;
  --ink:#2b2b2b;
  --text:#555;
  --muted:#888;
  --line:#dcdcdc;
  --panel:#f3f3f3;
  --footer:#262626;
}
*{box-sizing:border-box;margin:0;padding:0}
html,body{width:839px;height:1200px;overflow:hidden}
body{font-family:'Open Sans',Arial,sans-serif;color:var(--text);background:#fff;position:relative;font-size:10px}
.abs{position:absolute}
.header{left:0;top:0;width:839px;height:78px;background:linear-gradient(#ececec,#fff)}
.brand{left:78px;top:14px;display:flex;align-items:center;gap:8px}
.brand-mark{width:30px;height:30px;background:var(--red);border-radius:50%}
.brand-name{font-size:20px;font-weight:700;color:var(--ink);letter-spacing:-.3px}
.contact{right:100px;top:39px;font-size:8.5px;display:flex;gap:16px;align-items:center}
.contact a{color:var(--red);text-decoration:none}
.contact span{display:flex;align-items:center;gap:4px;color:var(--text)}
.nav{left:77px;top:89px;display:flex;border:1px solid var(--line);height:28px}
.nav a{display:flex;align-items:center;justify-content:center;font-size:9px;color:var(--ink);text-decoration:none;border-right:1px solid var(--line);height:100%}
.nav a:last-child{border-right:none}
.nav a.active{background:var(--red);color:#fff;font-weight:600}
.hero{left:77px;top:126px;width:685px;height:244px;background:linear-gradient(100deg,#bdbdbd 0%,#8a8170 35%,#c49a2a 50%,#6f6a60 65%,#d9d9d9 85%,#b55030 100%)}
.caption{left:77px;top:186px;width:267px;height:126px;background:rgba(30,30,30,.85);color:#fff;padding:12px 16px}
.caption h1{font-weight:400;font-size:21px;line-height:23px}
.caption p{font-size:9.5px;line-height:14px;margin-top:10px;color:#eee}
.dots{left:77px;top:314px;width:131px;height:19px;background:rgba(20,20,20,.85);display:flex;gap:5px;align-items:center;padding-left:26px}
.dots i{width:5px;height:5px;background:#fff}
.dots i.on{background:var(--red)}
.welcome{left:77px;top:382px;width:685px;height:68px;background:var(--panel);border:1px solid var(--line);border-left:3px solid var(--red);padding:9px 14px}
.welcome h2{font-weight:400;font-size:14.5px;color:var(--ink)}
.welcome p{font-size:9px;line-height:13px;margin-top:5px;width:540px}
.btn-dark{right:92px;top:404px;background:#111;color:#fff;font-size:8.5px;padding:6px 10px;border-radius:2px}
.sec-head{font-size:13px;font-weight:600;color:var(--ink)}
.sec-head em{font-size:7.5px;font-weight:400;color:var(--orange)}
.sec-line{height:1px;background:var(--line)}
.arrows{display:flex;gap:1px}
.arrows b{width:13px;height:13px;background:#ccc;color:#fff;font-size:8px;display:flex;align-items:center;justify-content:center;font-weight:400}
.arrows b+b{background:#999}
.service{width:160px;text-align:center}
.service svg{height:30px}
.service h3{font-size:11px;font-weight:400;color:var(--ink);margin-top:6px}
.service p{font-size:9px;line-height:10.5px;color:var(--muted);margin-top:11px}
.project{width:154px}
.project .photo{width:154px;height:91px}
.project h3{font-size:10.5px;font-weight:400;color:var(--ink);margin-top:14px}
.project p{font-size:9px;line-height:10.5px;color:var(--muted);margin-top:9px}
.news p{font-size:8px;line-height:13px;color:var(--ink)}
.input{left:80px;top:972px;width:255px;height:21px;border:1px solid var(--line);font-size:8px;color:#999;padding:4px 8px}
.subscribe{left:342px;top:972px;width:60px;height:21px;background:var(--orange);color:#fff;font-size:8.5px;display:flex;align-items:center;justify-content:center}
.note{left:80px;top:1004px;font-size:6.5px;font-style:italic;color:var(--muted)}
.note b{color:var(--red);font-weight:400}
.quote{left:440px;top:934px;width:322px;height:66px;background:var(--panel);border:1px solid var(--line);padding:12px 18px 0 29px;font-family:'Noto Serif',Georgia,serif;font-style:italic;font-size:9px;line-height:15px;color:var(--text)}
.quote a{color:var(--orange);text-decoration:none}
.author{left:662px;top:1010px;font-size:8px;line-height:11px;color:var(--ink)}
.author span{color:var(--muted)}
.partners{left:77px;top:1076px;width:685px;height:56px;display:flex;justify-content:space-between;align-items:center}
.partner{display:flex;align-items:center;gap:5px;font-size:10px;font-weight:600;color:#666;width:108px;justify-content:center}
.partner i{width:10px;height:10px;background:#bbb;border-radius:50%}
.shadow{left:77px;top:1050px;width:685px;height:8px;background:radial-gradient(ellipse at top,rgba(0,0,0,.08),transparent 70%)}
.footer{left:0;top:1160px;width:839px;height:40px;background:var(--footer);color:#bbb;font-size:7.5px}
.footer nav{position:absolute;left:79px;top:17px;display:flex;gap:6px}
.footer nav span{color:#777}
.footer .copy{position:absolute;right:80px;top:17px}
</style>
</head>
<body>
<div class="abs header"></div>
<div class="abs brand"><span class="brand-mark"></span><span class="brand-name">Bright Harbor Advisory</span></div>
<div class="abs contact">
  <span><svg width="10" height="8" viewBox="0 0 10 8"><rect x=".5" y=".5" width="9" height="7" fill="none" stroke="#aaa"/><path d="M.5 .5 5 4.5 9.5 .5" fill="none" stroke="#aaa"/></svg><a>hello@brightharboradvisory.com.au</a></span>
  <span><svg width="10" height="10" viewBox="0 0 10 10"><path d="M2 1 4 3 3 4.5Q4.5 6.5 5.5 7L7 6 9 8 7.5 9.5Q3 9 .5 2.5Z" fill="#aaa"/></svg>+61 0400 555 019</span>
</div>

<nav class="abs nav">
  <a class="active" style="width:72px">HOME</a><a style="width:52px">Services</a><a style="width:60px">Benefits</a><a style="width:83px">Management</a><a style="width:65px">Planning</a><a style="width:79px">Optimization</a><a style="width:60px">Industry</a><a style="width:63px">Software</a><a style="width:72px">Contact Us</a><a style="width:76px">Recruitment</a>
</nav>

<div class="abs hero" role="img" aria-label="Photo of an engineer in a hard hat and safety vest reading plans at a construction site with a crane"></div>
<div class="abs caption"><h1>Projects Controls Management Systems</h1><p>We can design and implemented project controls management system to provide the structural frame work required to accurately monitor</p></div>
<div class="abs dots"><i></i><i></i><i></i><i></i><i class="on"></i><i></i></div>

<div class="abs welcome"><h2>Welcome to a Bright Harbor Advisory website solution</h2><p>Bright Harbor Advisory  Provides effective project controls and management sloutions for construction projects in Australia and Overseas. We provide services to both large multination companies and smaller privately owned businesses.</p></div>
<div class="abs btn-dark">Read More</div>

<div class="abs sec-head" style="left:77px;top:479px">Our Services <em>- View All Services »</em></div>
<div class="abs arrows" style="left:735px;top:482px"><b>‹</b><b>›</b></div>
<div class="abs sec-line" style="left:77px;top:506px;width:685px"></div>

<div class="abs service" style="left:76px;top:522px"><svg viewBox="0 0 32 30" width="32"><g fill="var(--red)"><rect x="0" y="12" width="5" height="18"/><rect x="7" y="8" width="5" height="22"/><rect x="14" y="4" width="5" height="26"/><rect x="21" y="0" width="5" height="30"/><rect x="28" y="10" width="4" height="20"/></g><path d="M7 20q2 3 0 5q-2-2 0-5z" fill="#fff"/></svg><h3>Oil &amp; Gas</h3><p>Lorem Ipsum is simply dummy text of the printing and typesetting industry.</p></div>
<div class="abs service" style="left:252px;top:522px"><svg viewBox="0 0 26 30" width="26"><path d="M6 4h10l6 6v18H4V6z" fill="none" stroke="var(--red)" stroke-width="3"/><rect x="15" y="0" width="6" height="5" fill="var(--red)"/><path d="M13 13q4 5 0 8q-4-3 0-8z" fill="var(--red)"/></svg><h3>Petrochemical</h3><p>Lorem Ipsum is simply dummy text of the printing and typesetting industry.</p></div>
<div class="abs service" style="left:428px;top:522px"><svg viewBox="0 0 30 30" width="30"><rect x="2" y="2" width="6" height="12" fill="var(--red)"/><path d="M2 12h26v18H2z" fill="var(--red)"/><path d="M10 4q8-4 16 2" stroke="var(--red)" stroke-width="3" fill="none"/><g fill="#fff"><rect x="14" y="18" width="2" height="6"/><rect x="18" y="18" width="2" height="6"/><rect x="22" y="18" width="2" height="6"/></g></svg><h3>New Industries</h3><p>Lorem Ipsum is simply dummy text of the printing and typesetting industry.</p></div>
<div class="abs service" style="left:606px;top:522px"><svg viewBox="0 0 32 30" width="32"><path d="M2 10q0-8 14-8t14 8v3h-6v-3H8v3H2z" fill="var(--red)"/><g fill="var(--red)"><rect x="8" y="14" width="4" height="3"/><rect x="14" y="14" width="4" height="3"/><rect x="20" y="14" width="4" height="3"/><rect x="8" y="19" width="4" height="3"/><rect x="14" y="19" width="4" height="3"/><rect x="20" y="19" width="4" height="3"/><rect x="8" y="24" width="4" height="3"/><rect x="14" y="24" width="4" height="3"/><rect x="20" y="24" width="4" height="3"/></g></svg><h3>Telecommunications</h3><p>Lorem Ipsum is simply dummy text of the printing and typesetting industry.</p></div>

<div class="abs sec-head" style="left:79px;top:656px">Selected Projects <em>- View All Projects »</em></div>
<div class="abs arrows" style="left:735px;top:660px"><b>‹</b><b>›</b></div>
<div class="abs sec-line" style="left:77px;top:683px;width:685px"></div>

<div class="abs project" style="left:78px;top:701px"><div class="photo" role="img" aria-label="Oil pump jack in a grassy field under blue sky" style="background:linear-gradient(#5f8fc4 0%,#9bbbd8 55%,#b79a44 60%,#8a7530 100%)"></div><h3>Identify Project risks</h3><p>Lorem Ipsum is simply dummy text of the printing and typesetting industry.</p></div>
<div class="abs project" style="left:256px;top:701px"><div class="photo" role="img" aria-label="Refinery with long steel pipelines" style="background:linear-gradient(#d6d9dc 0%,#b9bcbf 40%,#8a8f8a 60%,#c5c3bc 100%)"></div><h3>Plan &amp; Control Budgets</h3><p>Lorem Ipsum is simply dummy text of the printing and typesetting industry.</p></div>
<div class="abs project" style="left:433px;top:701px"><div class="photo" role="img" aria-label="Blue-lit industrial pipework interior" style="background:linear-gradient(135deg,#0d3b6e,#3aa0e0 50%,#0b2b52)"></div><h3>Stream line processes</h3><p>Lorem Ipsum is simply dummy text of the printing and typesetting industry.</p></div>
<div class="abs project" style="left:608px;top:701px"><div class="photo" role="img" aria-label="Cart loaded with coal at a mine" style="background:linear-gradient(#6b6e5c,#3a3a36 50%,#1e1e1e)"></div><h3>Coal</h3><p>Lorem Ipsum is simply dummy text of the printing and typesetting industry.</p></div>

<div class="abs sec-head" style="left:80px;top:887px">Newsletter Subscription</div>
<div class="abs sec-line" style="left:80px;top:914px;width:322px"></div>
<div class="abs news" style="left:80px;top:933px;width:320px"><p>Subscribe to our email newsletter for useful tips and valuable resources sent out every second Monday.</p></div>
<div class="abs input">Enter your email address here ...</div>
<div class="abs subscribe">Subscribe</div>
<div class="abs note"><b>*</b> Check your spam folder if the mail does not arrive.</div>

<div class="abs sec-head" style="left:440px;top:887px">Testimonials <em>- View All Testimonials »</em></div>
<div class="abs arrows" style="left:734px;top:891px"><b>‹</b><b>›</b></div>
<div class="abs sec-line" style="left:440px;top:914px;width:322px"></div>
<div class="abs quote"><span style="position:absolute;left:11px;top:6px;font-size:16px;color:#bbb">“</span>Great theme! Very intuitive, clean code, very well-organized documentation – I would highly recommend getting this theme; it's ideal for further customization! <a>Read More ...</a></div>
<div class="abs author">Mara Ellison,<br><span>NorthQuill</span></div>

<div class="abs shadow"></div>
<div class="abs partners">
  <div class="partner"><i></i>Southline Energy</div>
  <div class="partner">Verano Fuels</div>
  <div class="partner">Crestmark Mining</div>
  <div class="partner">Halvern Alliance</div>
  <div class="partner"><i></i>Oakridge Resources</div>
  <div class="partner">Pindar Metals</div>
</div>

<footer class="abs footer">
  <nav>Home <span>|</span> Services <span>|</span> Benefits <span>|</span> Management <span>|</span> Planning <span>|</span> Optimization <span>|</span> Industry <span>|</span> Software <span>|</span> Contact Us</nav>
  <div class="copy">Copyright 2013 Bright Harbor Advisory | SEO</div>
</footer>
</body>
</html>
```